New flavour! New packaging for Velocity Energy Drink!

We need a new packaging designed to show off our new grape flavored energy drink! It will require box design with matching sachets!

Established in 2018 we are a fully Australian owned and operated business that started out with 2 gamers that got sick and tired of sugary energy drinks OR expensive powder from the USA.

We are an energy drink in the esports and gaming space. Our new product is an energy drink in powder in boxes of 30 sachets (please see attached for product example)

Please see example 1 and 2 for our competitors product. We would ideally like to go a bit more minimalist than them but still have a great color pop on black backing.

Target Market(s)

Gamer's and esports athletes between the ages or 18-30

Font styles to use
Sans Serif
Other font styles liked:
• Helvetica

Colors
886aae
ffffff

Requirements
Must have
• Black base/background.
• Vibrant purple N in the Velocity Logo.
• Same or slightly different shades of purple for some text and highlights.
• Black, white and some shades of a vibrant purple (for the grape flavor)
• ingredients list (may need to be reformatted to suit)
• Please see attached for legislative requirements on the box and sachets.
Nice to have
• minimalist design but enough to be eye catching and somewhat playful
• Twitter: @VLCT_FUEL
• Instagram: @VLCT_FUEL
• Facebook: @VLCTFUEL
Should not have
• OTHER COLORS.
• Overly complex designs.

```html
<!DOCTYPE html>
<html lang="en">
<head>
<meta charset="utf-8">
<title>Velocity Energy Drink – Grape Packaging</title>
<link rel="stylesheet" href="https://fonts.googleapis.com/css2?family=Exo+2:ital,wght@0,400;0,600;0,800;1,700&display=swap">
<style>
  :root {
    --stage: #e9e9ea;
    --stage-shadow: #bdbdbf;
    --black: #0c0a0d;
    --black-soft: #1b181d;
    --grey-type: #4a474d;
    --white: #ffffff;
    --purple: #886aae;
    --purple-vivid: #7a2fd0;
    --purple-deep: #5a1fa0;
  }
  * { box-sizing: border-box; margin: 0; padding: 0; }
  html, body { width: 1200px; height: 1061px; overflow: hidden; }
  body {
    background: linear-gradient(180deg, var(--stage) 0%, var(--stage) 60%, var(--stage-shadow) 100%);
    font-family: "Exo 2", "Helvetica Neue", Arial, sans-serif;
    position: relative;
  }

  /* ---------- Box front panel ---------- */
  .box-front {
    position: absolute;
    left: 110px; top: 150px;
    width: 560px; height: 760px;
    background: var(--black);
    overflow: hidden;
    box-shadow: 0 30px 60px rgba(0,0,0,.35);
  }
  .type-wall {
    position: absolute;
    inset: 40px 0 auto 0;
    height: 420px;
    background: radial-gradient(ellipse at 50% 45%, #3a373d 0%, var(--black-soft) 45%, var(--black) 80%);
  }
  .brand-lockup {
    position: absolute;
    left: 0; right: 0; top: 200px;
    text-align: center;
  }
  .brand-name {
    font-weight: 800;
    font-size: 92px;
    letter-spacing: 1px;
    color: var(--white);
    line-height: 1;
    text-transform: uppercase;
  }
  .brand-sub {
    margin-top: 10px;
    font-weight: 600;
    font-size: 20px;
    letter-spacing: 8px;
    color: var(--white);
    text-transform: uppercase;
  }
  .flavour {
    position: absolute;
    left: 40px; top: 500px;
    color: var(--purple);
    font-style: italic;
    font-weight: 700;
  }
  .flavour-name { font-size: 30px; letter-spacing: 2px; }
  .flavour-extras {
    display: flex; align-items: center; gap: 10px;
    margin-top: 8px;
  }
  .flavour-amp { font-size: 56px; line-height: 1; }
  .flavour-list { font-size: 26px; line-height: 1.05; letter-spacing: 2px; }
  .accent-square {
    position: absolute;
    right: 60px; top: 500px;
    width: 150px; height: 150px;
    background: var(--purple);
  }
  .tagline {
    position: absolute;
    left: 40px; bottom: 48px;
    color: var(--white);
    font-size: 15px;
    font-weight: 600;
    letter-spacing: 4px;
    line-height: 1.5;
    text-transform: uppercase;
  }
  .net-weight {
    position: absolute;
    right: 60px; bottom: 40px;
    color: var(--white);
    text-align: center;
    font-weight: 800;
    line-height: 1.05;
  }
  .net-weight-total { font-size: 34px; letter-spacing: 2px; }
  .net-weight-split { font-size: 18px; letter-spacing: 3px; }

  /* ---------- Sachets ---------- */
  .sachet {
    position: absolute;
    width: 150px; height: 640px;
    background: var(--black);
    box-shadow: 0 24px 40px rgba(0,0,0,.35);
    overflow: hidden;
  }
  .sachet--back { left: 790px; top: 300px; }
  .sachet--front { left: 950px; top: 230px; }
  .sachet-seal {
    position: absolute; left: 0; right: 0;
    height: 70px;
    background: linear-gradient(180deg, var(--purple-vivid), var(--purple-deep));
  }
  .sachet-seal--top { top: 0; }
  .sachet-seal--bottom { bottom: 0; }
  .sachet-body {
    position: absolute; left: 0; right: 0; top: 70px; bottom: 70px;
    background: radial-gradient(ellipse at 50% 55%, #3a373d 0%, var(--black-soft) 50%, var(--black) 90%);
  }
  .sachet-lockup {
    position: absolute;
    left: 50%; top: 50%;
    transform: translate(-50%, -50%) rotate(-90deg);
    white-space: nowrap;
    text-align: left;
  }
  .sachet-name {
    font-weight: 800;
    font-size: 62px;
    color: var(--white);
    line-height: 1;
    text-transform: uppercase;
  }
  .sachet-sub {
    margin-top: 4px;
    font-weight: 600;
    font-size: 13px;
    letter-spacing: 6px;
    color: var(--white);
    text-align: right;
    text-transform: uppercase;
  }
</style>
</head>
<body>
  <section class="box-front" aria-label="Velocity Energy Drink grape box, front panel">
    <div class="type-wall" role="img" aria-label="Embossed repeating typography backdrop: grape, purple drink, gaming, @VLCT_FUEL"></div>
    <div class="brand-lockup">
      <div class="brand-name">Velocity</div>
      <div class="brand-sub">Energy Drink</div>
    </div>
    <div class="flavour">
      <div class="flavour-name">Grape flavour</div>
      <div class="flavour-extras">
        <span class="flavour-amp">&amp;</span>
        <span class="flavour-list">Ginseng<br>Caffeine</span>
      </div>
    </div>
    <div class="accent-square" aria-hidden="true"></div>
    <p class="tagline">For gamers<br>By gamers</p>
    <div class="net-weight">
      <div class="net-weight-total">150g</div>
      <div class="net-weight-split">30x5g</div>
    </div>
  </section>

  <article class="sachet sachet--back" aria-label="Grape sachet">
    <div class="sachet-seal sachet-seal--top"></div>
    <div class="sachet-body" role="img" aria-label="Embossed repeating typography backdrop"></div>
    <div class="sachet-lockup">
      <div class="sachet-name">Velocity</div>
      <div class="sachet-sub">Energy Drink</div>
    </div>
    <div class="sachet-seal sachet-seal--bottom"></div>
  </article>

  <article class="sachet sachet--front" aria-label="Grape sachet">
    <div class="sachet-seal sachet-seal--top"></div>
    <div class="sachet-body" role="img" aria-label="Embossed repeating typography backdrop"></div>
    <div class="sachet-lockup">
      <div class="sachet-name">Velocity</div>
      <div class="sachet-sub">Energy Drink</div>
    </div>
    <div class="sachet-seal sachet-seal--bottom"></div>
  </article>
</body>
</html>
```